Stridewell Outfitters Stationary

At Stridewell Outfit, we know that rehab technology is much more than a tool or machine. It’s mobility for your body and productivity and freedom for your lifestyle to reclaim your life. That’s why we specialize in custom power and manual wheelchairs, scooters, complex seating and positioning, standers, and bathroom equipment that all help you reclaim your life.

Our rehab equipment includes custom power wheelchairs offering complex, customized seating and positioning systems with an array of specialized electronic control features. With a certified staff of Assistive Technology Professionals (ATPs) and technical repair department, we provide knowledgeable assistance to make sure you get the right products needed to reclaim your life – delivered on time, right to your door.

```html
<!DOCTYPE html>
<html lang="en">
<head>
<meta charset="utf-8">
<title>Stridewell Outfitters Stationery</title>
<link href="https://fonts.googleapis.com/css2?family=Exo+2:wght@400;600&family=Roboto:wght@400;700&display=swap" rel="stylesheet">
<style>
  :root {
    --navy: #0b3257;
    --green: #8cc63f;
    --paper: #ffffff;
    --backdrop: #eeeeee;
    --ink: #3a3a3a;
  }
  * { margin: 0; padding: 0; box-sizing: border-box; }
  html, body { width: 1200px; height: 937px; overflow: hidden; }
  body { background: var(--backdrop); position: relative; font-family: "Roboto", Arial, sans-serif; color: var(--ink); }

  .piece { position: absolute; background: var(--paper); overflow: hidden; }
  .wave { position: absolute; left: 0; bottom: 0; width: 100%; }
  .wave svg { display: block; width: 100%; height: 100%; }

  .brand { position: absolute; display: flex; align-items: center; gap: 0.3em;
           font-family: "Exo 2", sans-serif; font-weight: 600; color: var(--navy); white-space: nowrap; }
  .brand-dot { width: 0.55em; height: 0.55em; border-radius: 50%; background: var(--green); flex: none; }

  .web { position: absolute; font-family: "Exo 2", sans-serif; color: var(--paper); letter-spacing: 0.14em; white-space: nowrap; }

  /* Letterhead */
  .letterhead { left: 184px; top: 66px; width: 388px; height: 546px; }
  .letterhead .brand { left: 42px; top: 40px; font-size: 15px; }
  .letter { position: absolute; left: 37px; top: 140px; width: 300px; font-size: 5.6px; line-height: 7.6px; }
  .letter p { margin-bottom: 9px; }
  .letter .date { margin-bottom: 7px; }
  .letter .salute { font-weight: 700; margin-bottom: 0; }
  .letter .para-gap { margin-bottom: 24px; }
  .signature { width: 26px; height: 14px; margin: 4px 0 4px; display: block; }
  .letter .signer { font-weight: 700; margin-bottom: 0; }
  .letter .tight { margin-bottom: 0; }
  .letterhead .wave { height: 108px; }
  .contact { position: absolute; right: 10px; bottom: 8px; text-align: right; color: var(--paper); font-size: 5.4px; line-height: 10px; }
  .contact .addr { line-height: 7px; margin-bottom: 4px; font-size: 6px; }
  .contact .row { display: flex; justify-content: flex-end; align-items: center; gap: 3px; }
  .icon { width: 6px; height: 6px; fill: var(--paper); }

  /* Folder */
  .folder { left: 636px; top: 40px; width: 459px; height: 578px; }
  .folder .brand { left: 100px; top: 280px; font-size: 30px; }
  .folder .wave { height: 215px; }
  .folder .web { right: 16px; bottom: 10px; font-size: 12px; }

  /* Business cards */
  .card { width: 177px; height: 100px; border-radius: 8px; }
  .card-front { left: 45px; top: 658px; }
  .card-front .brand { left: 8px; top: 18px; font-size: 9px; }
  .card-front .wave { height: 82px; }
  .card-person { position: absolute; left: 8px; top: 72px; font-size: 5px; line-height: 6px; color: var(--navy); }
  .card-person strong { display: block; font-size: 5.6px; }
  .card-contact { position: absolute; right: 7px; top: 50px; text-align: right; color: var(--paper); font-size: 3.6px; line-height: 6.4px; }
  .card-contact p { display: flex; justify-content: flex-end; align-items: center; gap: 2px; }
  .card-contact .icon { width: 4px; height: 4px; }
  .card-back { left: 45px; top: 785px; }
  .card-back .brand { left: 50%; top: 50%; transform: translate(-50%, -50%); font-size: 11px; }

  /* Envelope front */
  .envelope { left: 265px; top: 672px; width: 432px; height: 210px; }
  .envelope .brand { left: 17px; top: 38px; font-size: 17px; }
  .envelope .wave { height: 192px; }
  .envelope .web { right: 14px; bottom: 10px; font-size: 9px; }

  /* Envelope back */
  .envelope-back { left: 737px; top: 672px; width: 432px; height: 209px; }
  .flap { position: absolute; left: 0; top: 0; width: 100%; height: 72px; background: var(--navy); border-radius: 0 0 34px 34px; }
  .flap .web { left: 0; right: 0; top: 30px; text-align: center; font-size: 11px; }
</style>
</head>
<body>

<svg width="0" height="0" style="position:absolute" aria-hidden="true">
  <defs>
    <symbol id="wave" viewBox="0 0 100 100" preserveAspectRatio="none">
      <path d="M0,93 C40,90 52,8 100,0 L100,100 L0,100 Z" fill="#8cc63f"/>
      <path d="M0,97 C42,95 55,13 100,6 L100,100 L0,100 Z" fill="#ffffff"/>
      <path d="M0,99 C44,98 58,19 100,11 L100,100 L0,100 Z" fill="#0b3257"/>
      <path d="M0,100 C46,99 61,26 100,18" fill="none" stroke="#ffffff" stroke-width="1" vector-effect="non-scaling-stroke"/>
    </symbol>
    <symbol id="i-phone" viewBox="0 0 10 10"><path d="M2 1 L4 1 L5 3.5 L3.8 4.5 C4.4 5.8 5 6.4 6.3 7 L7.3 5.8 L9.5 6.8 L9.5 9 C5 9.5 0.6 5 1 1 Z"/></symbol>
    <symbol id="i-mobile" viewBox="0 0 10 10"><path d="M3 0.5 H7 V9.5 H3 Z M3.8 1.5 V7.5 H6.2 V1.5 Z"/></symbol>
    <symbol id="i-fax" viewBox="0 0 10 10"><path d="M2.5 1 H7.5 V4 H9 V8.5 H1 V4 H2.5 Z M3.3 1.8 V4 H6.7 V1.8 Z"/></symbol>
    <symbol id="i-mail" viewBox="0 0 10 10"><path d="M0.5 2 H9.5 V8 H0.5 Z M1.3 2.6 L5 5.4 L8.7 2.6 Z"/></symbol>
    <symbol id="i-web" viewBox="0 0 10 10"><circle cx="5" cy="5" r="4.3"/></symbol>
  </defs>
</svg>

<!-- Letterhead -->
<section class="piece letterhead">
  <div class="brand"><span class="brand-dot"></span>Stridewell Outfitters</div>
  <div class="letter">
    <p class="date">July 2, 2012</p>
    <p class="salute">Dear Client,</p>
    <p>Harbor Court, Elm St., Fairview</p>
    <p>We are pleased to confirm your custom seating assessment for next month. Our certified team will review your mobility needs, measure your chair and prepare a fitting plan. Every device is checked by our repair department before delivery, so you can expect a safe and comfortable ride from day one. Please keep this letter for your records and call us with any questions.</p>
    <p class="para-gap">Your appointment details and a product guide are enclosed with this letter.</p>
    <p>Thank you for choosing us as your partner in rehab technology. We will stay in touch through every step of the process, from the first visit to final adjustments, and our support line remains open whenever your equipment needs attention.</p>
    <p class="tight">Best Regards,</p>
    <svg class="signature" viewBox="0 0 26 14" aria-hidden="true"><path d="M2 12 C4 2 6 2 6 8 C7 12 9 6 11 9 C13 11 16 7 24 9" fill="none" stroke="#333" stroke-width="0.7"/></svg>
    <p class="signer">Dana Whitlow</p>
    <p class="tight">Director</p>
    <p>Harbor Court, Elm St., Fairview</p>
  </div>
  <div class="wave"><svg><use href="#wave"/></svg></div>
  <div class="contact">
    <p class="addr">420 Crestline Ave,<br>Suite 12</p>
    <p class="row">555 014 2290 <svg class="icon"><use href="#i-phone"/></svg></p>
    <p class="row">555 014 2291 <svg class="icon"><use href="#i-mobile"/></svg></p>
    <p class="row">555 014 2292 <svg class="icon"><use href="#i-fax"/></svg></p>
    <p class="row">hello@stridewelloutfit.com <svg class="icon"><use href="#i-mail"/></svg></p>
    <p class="row">www.stridewelloutfit.com <svg class="icon"><use href="#i-web"/></svg></p>
  </div>
</section>

<!-- Presentation folder -->
<section class="piece folder">
  <div class="brand"><span class="brand-dot"></span>Stridewell Outfitters</div>
  <div class="wave"><svg><use href="#wave"/></svg></div>
  <p class="web">www.stridewelloutfit.com</p>
</section>

<!-- Business card front -->
<section class="piece card card-front">
  <div class="brand"><span class="brand-dot"></span>Stridewell Outfitters</div>
  <div class="wave"><svg><use href="#wave"/></svg></div>
  <p class="card-person"><strong>MARCUS ELLERY</strong>Managing Director</p>
  <div class="card-contact">
    <p>420 Crestline Ave, Suite 12</p>
    <p>555 014 2290 <svg class="icon"><use href="#i-phone"/></svg></p>
    <p>555 014 2291 <svg class="icon"><use href="#i-mobile"/></svg></p>
    <p>555 014 2292 <svg class="icon"><use href="#i-fax"/></svg></p>
    <p>hello@stridewelloutfit.com <svg class="icon"><use href="#i-mail"/></svg></p>
    <p>www.stridewelloutfit.com <svg class="icon"><use href="#i-web"/></svg></p>
  </div>
</section>

<!-- Business card back -->
<section class="piece card card-back">
  <div class="brand"><span class="brand-dot"></span>Stridewell Outfitters</div>
</section>

<!-- Envelope front -->
<section class="piece envelope">
  <div class="brand"><span class="brand-dot"></span>Stridewell Outfitters</div>
  <div class="wave"><svg><use href="#wave"/></svg></div>
  <p class="web">www.stridewelloutfit.com</p>
</section>

<!-- Envelope back -->
<section class="piece envelope-back">
  <div class="flap"><p class="web">www.stridewelloutfit.com</p></div>
</section>

</body>
</html>
```